Commercial Construction Company

We need a business card design based on our current logo. We are a commercial general contractor based in Southern California that specializes in bank remodels. We would like to see designs that incorporate dark blue. The final design should portray an image of professionalism and quality.

If possible, I would like to add metallic foil to the design. Thank you

```html
<!DOCTYPE html>
<html lang="en">
<head>
<meta charset="utf-8">
<title>Halvern Commercial Builders – Business Card</title>
<link rel="stylesheet" href="https://fonts.googleapis.com/css2?family=Montserrat:wght@700;800&family=Arimo:wght@400&display=swap">
<style>
  :root {
    --stage: #2c2f34;
    --brand-blue: #0a4a80;
    --paper: #ffffff;
    --silver: #a3a3a3;
    --ink: #111111;
  }
  html, body {
    margin: 0;
    width: 1200px;
    height: 1000px;
    overflow: hidden;
    background: var(--stage);
  }
  .stage {
    position: relative;
    width: 1200px;
    height: 1000px;
  }
  .card {
    position: absolute;
    left: 230px;
    width: 740px;
    height: 423px;
    border-radius: 22px;
    overflow: hidden;
    background: var(--brand-blue);
    box-shadow: 0 14px 30px rgba(0,0,0,0.45);
  }
  .card--back { top: 50px; }
  .card--front { top: 523px; }

  /* Back: company name centred */
  .wordmark {
    position: absolute;
    inset: 0;
    display: flex;
    flex-direction: column;
    align-items: center;
    justify-content: center;
    font-family: "Montserrat", sans-serif;
    font-weight: 800;
    color: var(--paper);
    text-align: center;
  }
  .wordmark__main { font-size: 66px; letter-spacing: 2px; line-height: 1; }
  .wordmark__sub { font-size: 14px; letter-spacing: 6px; margin-top: 12px; }

  /* Front */
  .accent-bar {
    position: absolute;
    left: 22px;
    top: 40px;
    width: 12px;
    height: 42px;
    background: var(--silver);
  }
  .person__name {
    position: absolute;
    left: 50px;
    top: 36px;
    margin: 0;
    font-family: "Montserrat", sans-serif;
    font-weight: 800;
    font-size: 30px;
    color: var(--silver);
    letter-spacing: 0.5px;
  }
  .person__title {
    position: absolute;
    left: 50px;
    top: 78px;
    margin: 0;
    font-family: "Arimo", sans-serif;
    font-size: 20px;
    color: var(--paper);
  }
  .address {
    position: absolute;
    left: 50px;
    top: 175px;
    margin: 0;
    font-family: "Arimo", sans-serif;
    font-style: normal;
    font-size: 21px;
    line-height: 1.25;
    color: var(--paper);
  }
  .contacts {
    position: absolute;
    left: 50px;
    top: 268px;
    margin: 0;
    padding: 0;
    list-style: none;
    font-family: "Arimo", sans-serif;
    font-size: 20px;
    line-height: 1.3;
    color: var(--paper);
  }
  .contacts li { display: flex; align-items: center; gap: 8px; }
  .contacts svg { width: 15px; height: 15px; fill: var(--paper); flex: none; }

  .front-panel {
    position: absolute;
    left: 0; top: 0;
    width: 740px; height: 423px;
  }
  .front-wordmark {
    position: absolute;
    left: 505px;
    top: 175px;
    width: 210px;
    display: flex;
    flex-direction: column;
    align-items: center;
    font-family: "Montserrat", sans-serif;
    font-weight: 800;
    color: var(--ink);
    text-align: center;
  }
  .front-wordmark__main { font-size: 46px; letter-spacing: 1px; line-height: 1; }
  .front-wordmark__sub { font-size: 10px; letter-spacing: 4px; margin-top: 10px; }
</style>
</head>
<body>
<main class="stage">

  <section class="card card--back" aria-label="Card back">
    <div class="wordmark">
      <span class="wordmark__main">HALVERN</span>
      <span class="wordmark__sub">COMMERCIAL BUILDERS</span>
    </div>
  </section>

  <section class="card card--front" aria-label="Card front">
    <svg class="front-panel" viewBox="0 0 740 423" aria-hidden="true">
      <circle cx="690" cy="300" r="300" fill="var(--paper)"/>
    </svg>

    <span class="accent-bar"></span>
    <h1 class="person__name">MARCUS DELANEY</h1>
    <p class="person__title">FOUNDER/CEO</p>

    <address class="address">218 Harbor Point Avenue Long<br>Beach, CA 90802</address>

    <ul class="contacts">
      <li><svg viewBox="0 0 16 16"><path d="M3.5 1.5l2.6 2.6-1.5 1.8a9 9 0 0 0 5.5 5.5l1.8-1.5 2.6 2.6-1.8 2A11.5 11.5 0 0 1 1.5 3.3z"/></svg>562-555-0148</li>
      <li><svg viewBox="0 0 16 16"><path d="M4.5 1h7a1 1 0 0 1 1 1v12a1 1 0 0 1-1 1h-7a1 1 0 0 1-1-1V2a1 1 0 0 1 1-1zm.5 2v9h6V3z"/></svg>(office) 562-555-0193</li>
      <li><svg viewBox="0 0 16 16"><path d="M1 3h14v10H1zm1.5 1.4V12h11V4.4L8 8.6z"/></svg>marcus@halverncommercial.com</li>
      <li><svg viewBox="0 0 16 16"><path d="M8 1a7 7 0 1 0 0 14A7 7 0 0 0 8 1zm0 1.5a5.5 5.5 0 0 1 0 11 5.5 5.5 0 0 1 0-11zM4 8h8v1H4zm3.5-5h1v10h-1z"/></svg>www.halverncommercial.com</li>
    </ul>

    <div class="front-wordmark">
      <span class="front-wordmark__main">HALVERN</span>
      <span class="front-wordmark__sub">COMMERCIAL BUILDERS</span>
    </div>
  </section>

</main>
</body>
</html>
```